An expert for Professional and Technical Evaluation of Painting Work Needs a New Letterhead Design

I own a mid-sized painting company and also work as an expert for professional and technical evaluation of painting work in the area of Zurich.

Please read the project description and the must-have-requirements carefully!

I attached 1 PDF which will help you create a new letterhead design:

THE NEW DESIGN DOESN'T NEED A LOGO! (Because it won't represent a company, it represents only a service)
Updates

Dear designers We had a discussion about the location/placement of the design and came to the conclusion that we only want the design to be in the header area of the A4-paper. We would be glad to receive some revised version of your designs. Thank you and kind regards!

Project Deadline Extended
Reason: Due to the fact that only 20% of the designer have understood the brief and submitted designs that have met the requirements we decided to extend the contest deadline.

Project Deadline Extended
Reason: A great deal of good designs were submitted in the last few days. A big thank you to all the participating designers for your good work. We need a few more days to discuss some changes with certain designers and to decide which design will win.

Target Market(s)

(Insurance) Companies, partly also private clients.

Industry/Entity Type

Painting

Colors

Designer to choose colors to be used in the design.

Requirements
Must have
• All information (text, phone numbers, ...) of the old design ("old_letterhead_design.pdf") has also to be in the new one. Additional to that there are a few changes:
The phone numbers "01 583 61 47" and "01 583 61 37" change to "044 583 61 47" and "044 583 61 37". And please mention also this email address: gutachten@valmorkeller.example .

- The design should only be in the header-area of the A4-paper. An the background color of the A4-paper will be white.

- The design should consist of two designs. One for the first page and a smaller version of the design for the following pages.

- THE NEW DESIGN DOESN'T NEED A LOGO! You can make a design with geometric forms, ...

- The new design should have a juridical look. It should only contain colors like brown, fawn, black, light green, ...... colors which look serious/reliable.
Nice to have
• Geometric Forms, Symbols or other design elements.

- It would also be nice to have some design elements which emphasize the kind of work we are offering.

```html
<!DOCTYPE html>
<html lang="de">
<head>
<meta charset="utf-8">
<title>Valmor Keller – Briefkopf</title>
<link rel="stylesheet" href="https://fonts.googleapis.com/css2?family=Architects+Daughter&family=Lora:wght@400;700&display=swap">
<style>
  :root {
    --backdrop: #ececea;
    --paper: #ffffff;
    --ink: #151515;
    --band: #111111;
    --mint: #7fd6b4;
    --header-text: #f4f4f4;
    --body-text: #2a2a2a;
    --muted: #555555;
  }
  * { box-sizing: border-box; margin: 0; padding: 0; }
  html, body {
    width: 1200px; height: 800px; overflow: hidden;
    background: var(--backdrop);
  }
  .sheet {
    position: absolute; left: 338px; top: 30px;
    width: 524px; height: 740px;
    background: var(--paper);
    box-shadow: 0 2px 10px rgba(0,0,0,.08);
    font-family: "Lora", Georgia, serif;
    color: var(--body-text);
    overflow: hidden;
  }
  .header-band { position: absolute; left: 0; top: 0; width: 524px; height: 140px; }
  .header-band svg { position: absolute; left: 0; top: 0; }
  .brush-texture {
    position: absolute; left: 0; top: 56px; width: 90px; height: 52px;
    background: linear-gradient(90deg, rgba(17,17,17,0) 0%, rgba(17,17,17,.6) 50%, var(--band) 100%);
  }
  .sender {
    position: absolute; right: 232px; top: 42px;
    font-family: "Architects Daughter", cursive;
    color: var(--header-text);
    text-align: right;
    white-space: nowrap;
  }
  .sender-name { font-size: 17px; letter-spacing: 2px; line-height: 1; }
  .sender-title { font-size: 9px; letter-spacing: .5px; margin-top: 3px; }
  .contact {
    position: absolute; right: 14px; top: 10px;
    display: grid; grid-template-columns: auto auto; column-gap: 5px;
    font-family: "Architects Daughter", cursive;
    color: var(--header-text);
    font-size: 7.5px; line-height: 11px; letter-spacing: .3px;
    white-space: nowrap;
  }
  .contact dt { text-align: right; }
  .letter { position: absolute; left: 64px; top: 184px; width: 400px; font-size: 9.5px; line-height: 14px; }
  .date { font-weight: 700; margin-bottom: 36px; }
  .recipient { color: var(--muted); margin-bottom: 26px; font-style: normal; }
  .letter p { margin-bottom: 14px; text-align: justify; color: var(--muted); }
  .signature {
    width: 110px; height: 34px; margin-top: 26px;
    background: radial-gradient(ellipse at center, rgba(20,20,20,.18), rgba(20,20,20,0) 70%);
  }
  .signer { line-height: 12px; }
  .signer-name { font-weight: 700; color: var(--ink); }
</style>
</head>
<body>
  <main class="sheet">
    <header class="header-band">
      <svg width="524" height="140" viewBox="0 0 524 140" aria-hidden="true">
        <path d="M524 0 H150 C120 10 90 30 70 56 L70 110 C210 100 360 90 524 78 Z" fill="var(--band)"/>
        <path d="M250 98 C330 94 430 86 524 78 L524 83 C430 91 330 99 250 102 Z" fill="var(--mint)"/>
        <path d="M60 110 C120 108 180 105 230 102 L230 105 C180 108 120 111 60 113 Z" fill="var(--mint)" opacity=".8"/>
      </svg>
      <div class="brush-texture" role="img" aria-label="Rough black brush-stroke texture fading out to the left"></div>
      <div class="sender">
        <div class="sender-name">VALMOR KELLER</div>
        <div class="sender-title">eidg. dipl. Malermeister</div>
      </div>
      <dl class="contact">
        <dt>TELEFON</dt><dd>044 583 61 47</dd>
        <dt>FAX</dt><dd>044 583 61 37</dd>
        <dt>NATEL</dt><dd>079 412 55 90</dd>
        <dt>EMAIL</dt><dd>gutachten@valmorkeller.example</dd>
        <dt></dt><dd>Lindenweg 7 &nbsp;8305 Dietlikon</dd>
      </dl>
    </header>

    <article class="letter">
      <div class="date">Cartagena de Indias, October 31, 2013</div>
      <address class="recipient">
        Sr.<br>MARCO RIEDER<br>Web Master<br>City
      </address>
      <p>Lorem ipsum dolor sit amet, consetetur sadipscing elitr, sed diam nonumy eirmod tempor invidunt ut labore et dolore magna aliquyam erat, sed diam voluptua. At vero eos et accusam et justo duo dolores et ea rebum. Stet clita kasd gubergren, no sea takimata sanctus est lorem ipsum dolor sit amet. Lorem ipsum dolor sit amet, consetetur sadipscing elitr, sed diam nonumy eirmod tempor invidunt ut labore et dolore magna aliquyam erat, sed diam voluptua.</p>
      <p>At vero eos et accusam et justo duo dolores et ea rebum. Stet clita kasd gubergren, no sea takimata sanctus est lorem ipsum dolor sit amet. Lorem ipsum dolor sit amet, consetetur sadipscing elitr, sed diam nonumy eirmod tempor invidunt ut labore et dolore magna aliquyam erat, sed diam voluptua.</p>
      <p>Duis autem vel eum iriure dolor in hendrerit in vulputate velit esse molestie consequat, vel illum dolore eu feugiat nulla facilisis at vero eros et accumsan et iusto odio dignissim qui blandit praesent.</p>
      <p>Best regards,</p>
      <div class="signature" role="img" aria-label="Handwritten signature"></div>
      <div class="signer">
        <div class="signer-name">LENA BRUNNER</div>
        <div>Manager</div>
      </div>
    </article>
  </main>
</body>
</html>
```